Coach/consultant in conflict and challenge needs an enticing flyer

I need a double sided DL flyer design that will describe my work in helping people meet conflict and emotional challenge so they can learn and grow from these difficulties. I want to give a flavour of my style through fresh colours, repeated images used differently (the spiral), and a sense of positivity around conflict and difficulty. I want to attract people who are keen to do things differently and want to engage with creative processes rather than getting stuck in familiar patterns. My work is creative and often includes use of story, images and fables, so I want to convey that as well. I also place the work in a spiritual context, but grounded in practicality so I don't want it to seem New Age or flakey. I want something that seems innovative, professional and intriguing. I've included a sample of something I mocked up in word and also a copy of a flyer for Marla Quennet's Ember Gathering that inspired me to get a DL flyer. I want the design to communicate trust and transformation and engaging with fresh ways of doing things by moving past old habits

Target Market(s)

Mid 30s plus women and men who want to change their approach to conflict and emotional difficulties and are willing to take the creative and challenging journey to do that

Industry/Entity Type

Learn

Colors
acd136
00a990

Requirements
Must have
• a shift in the use of the spiral image,
• use of image of me (Norah)
• bright fresh colours olours that represent growth and transformation--I've suggested lime green as it suggests a sense of growth
• easy to read text
Nice to have
• Interesting non-traditional fonts perhaps text in a contemporary sans serif and another brush script font (like the Ember Gathering example)
• bleed to the edge and run off the page images or text
Should not have
• anything that represents too much tradition or stuckness

```html
<!DOCTYPE html>
<html lang="en">
<head>
<meta charset="utf-8">
<title>Norah Castellan – DL Flyer</title>
<link href="https://fonts.googleapis.com/css2?family=Alegreya:wght@400&family=Nunito+Sans:ital,wght@0,300;0,400;0,700;1,800&display=swap" rel="stylesheet">
<style>
  :root {
    --page-bg: #ecebe6;
    --lime: #acd136;
    --teal: #00a990;
    --brown: #8a4b2e;
    --brush-brown: #9a5a32;
    --brush-light: #b7784a;
    --ink-olive: #5e6a4e;
    --ink-hash: #66704f;
    --white: #ffffff;
    --photo-warm: #c9784a;
    --photo-grey: #a49a8c;
    --photo-orange: #d2582a;
  }
  * { box-sizing: border-box; margin: 0; padding: 0; }
  html, body { width: 1200px; height: 1080px; overflow: hidden; }
  body {
    background: var(--page-bg);
    font-family: "Nunito Sans", sans-serif;
    position: relative;
  }
  .flyer-side {
    position: absolute;
    width: 832px;
    height: 427px;
    overflow: hidden;
  }

  /* Front */
  .flyer-front { left: 147px; top: 66px; background: var(--lime); }
  .front-brush-art {
    position: absolute; left: 553px; top: 34px; width: 122px; height: 106px;
    border-radius: 18px;
    background: linear-gradient(135deg, var(--brush-light), var(--brush-brown));
  }
  .client-name {
    position: absolute; left: 133px; top: 62px;
    font-family: "Alegreya", serif; font-weight: 400; font-size: 30px; color: var(--brown);
  }
  .hashtags {
    position: absolute; left: 133px; top: 136px;
    font-size: 17px; font-weight: 300; color: var(--ink-hash);
    word-spacing: 3px;
  }
  .front-quote {
    position: absolute; left: 169px; top: 181px; width: 525px;
    font-size: 15.5px; line-height: 20px; color: var(--ink-olive);
  }
  .front-intro {
    position: absolute; left: 133px; top: 270px; width: 580px;
    font-size: 23px; line-height: 29px; font-weight: 300; color: var(--ink-olive);
  }

  /* Back */
  .flyer-back { left: 209px; top: 556px; background: var(--teal); }
  .back-band {
    position: absolute; left: 0; bottom: 0; width: 100%; height: 65px;
    background: var(--lime);
  }
  .back-copy {
    position: absolute; left: 30px; top: 58px; width: 520px;
    color: var(--white); font-size: 13px; line-height: 17px; font-weight: 300;
  }
  .back-copy p + p { margin-top: 17px; }
  .back-copy strong { font-weight: 700; }
  .credentials {
    position: absolute; left: 31px; top: 242px;
    color: var(--white); font-size: 13px; line-height: 17px; font-weight: 300;
  }
  .credentials strong { font-weight: 700; display: block; }
  .contact-phones {
    position: absolute; left: 31px; top: 296px;
    color: var(--white); font-size: 13px; line-height: 17px; font-weight: 700;
  }
  .contact-web {
    position: absolute; left: 216px; top: 305px;
    color: var(--white); font-size: 13px; line-height: 17px; font-weight: 700;
  }
  .services {
    position: absolute; left: 434px; top: 213px; z-index: 2;
    list-style: none; color: var(--white);
    font-size: 20px; line-height: 25px; font-weight: 800; font-style: italic;
  }
  .services li::before { content: "* "; }
  .portrait {
    position: absolute; left: 578px; top: 24px; width: 254px; height: 403px; z-index: 1;
    border-radius: 110px 110px 0 0;
    background: linear-gradient(180deg, var(--photo-grey) 0%, #d8b9a0 32%, var(--photo-warm) 52%, var(--photo-orange) 100%);
  }
</style>
</head>
<body>

<section class="flyer-side flyer-front" aria-label="Flyer front">
  <h1 class="client-name">Norah Castellan</h1>
  <div class="front-brush-art" role="img" aria-label="Brown brush-painted artwork"></div>
  <p class="hashtags">#courage &nbsp;#listening #creativity</p>
  <p class="front-quote">Challenge, change and conflict are a natural part of life. When we greet them with courage, and listen to what they tell us, we grow in wisdom, resilience and creativity.</p>
  <p class="front-intro">Norah Castellan is a coach, educator and mediator. She works with people who want to harvest the fruits of challenge and conflict so they live life differently.</p>
</section>

<section class="flyer-side flyer-back" aria-label="Flyer back">
  <div class="back-band"></div>
  <div class="back-copy">
    <p>Consult with Norah to address challenges in your life, relationship, group or organisation. Through listening, conversation and creative processes, you will discover what your challenge is asking of you. Norah Castellan is a skilled facilitator who works to shift people’s responses from reactivity to creativity.</p>
    <p>With many years’ experience in coaching and mentorship, mediation and narrative processes, Norah supports you to uncover unique responses to difficult situations.</p>
    <p>Talk to Norah <strong>0400 555 182</strong></p>
  </div>
  <p class="credentials"><strong>Norah Castellan</strong>PhD, MCR, BAppSci, DipHum, AssDipEd</p>
  <p class="contact-phones">0400 555 182 (m)<br>+61 3 9000 4417 (h)<br>ABN 12 345 678 90</p>
  <p class="contact-web">norah@norahcastellan.com<br>norahcastellan.com</p>
  <div class="portrait" role="img" aria-label="Photograph of Norah in an orange top, holding brush-painted artwork"></div>
  <ul class="services">
    <li>consultations</li>
    <li>workshops</li>
    <li>speaking</li>
    <li>articles</li>
  </ul>
</section>

</body>
</html>
```